Concrete Curbing Brochure Design Project

I would like to get a Tri-Fold Brochure piece put together to go over our new Concrete Curbing service. I have a sample design from another company that I like as well as a flyer that we currently have. I would like for this to have the benefits of concrete curbing, the different applications, the styles to choose from and the stamps available.

Target Market(s)

Home Owners and Commercial Business Owners

Industry/Entity Type

Concrete

Requirements
Must have
• The Brenwick Logo
Web address: www.brenwickyardworks.example
Phone Number-800-617-4928
Free Estimates

```html
<!DOCTYPE html>
<html lang="en">
<head>
<meta charset="utf-8">
<title>Concrete Curbing Brochure</title>
<link rel="stylesheet" href="https://fonts.googleapis.com/css2?family=Open+Sans:wght@400;600;700&family=Oswald:wght@700&display=swap">
<style>
  :root {
    --backdrop: #e4e4e4;
    --paper: #ffffff;
    --lime: #9dbf14;
    --lime-light: #c4dc5a;
    --lawn: #5f8a3a;
    --mulch: #a9825a;
    --shrub: #2f4a22;
    --brand-green: #1e6b45;
    --label-red: #e8262a;
    --ink: #2a2a2a;
    --outline: #1a1a1a;
  }
  * { box-sizing: border-box; margin: 0; padding: 0; }
  html, body { width: 1200px; height: 675px; overflow: hidden; }
  body {
    background: var(--backdrop);
    font-family: "Open Sans", sans-serif;
    position: relative;
  }
  .panel {
    position: absolute;
    top: 28px;
    width: 300px;
    height: 620px;
    overflow: hidden;
    box-shadow: 0 4px 14px rgba(0,0,0,.18);
  }

  /* Back panel */
  .back-panel {
    left: 270px;
    background: linear-gradient(180deg, var(--lime) 0%, var(--lime-light) 40%, #e9f0d2 62%, #f4f6ee 100%);
  }
  .snapshot {
    position: absolute;
    background: var(--paper);
    padding: 26px 10px 10px;
    box-shadow: 0 3px 8px rgba(0,0,0,.3);
  }
  .snapshot-label {
    position: absolute;
    top: 5px;
    left: 12px;
    color: var(--label-red);
    font-size: 14px;
    font-weight: 400;
  }
  .snapshot-photo { width: 100%; height: 100%; }
  .snapshot-beauty {
    left: 22px; top: 40px; width: 215px; height: 150px;
    transform: rotate(-7deg);
  }
  .snapshot-beauty .snapshot-photo {
    background: linear-gradient(160deg, var(--shrub) 0%, #55703a 40%, var(--mulch) 55%, var(--lawn) 75%, #7ea04e 100%);
  }
  .snapshot-value {
    left: 135px; top: 190px; width: 155px; height: 160px;
    transform: rotate(-4deg);
  }
  .snapshot-value .snapshot-photo {
    background: linear-gradient(170deg, #6d4b3a 0%, #5b6e34 45%, #c0683a 58%, #6f9342 72%, var(--lawn) 100%);
  }
  .yard-photo {
    position: absolute;
    left: 0; top: 330px; width: 300px; height: 290px;
    background: linear-gradient(180deg, rgba(150,180,110,0) 0%, #8fb06a 25%, var(--lawn) 45%, var(--mulch) 70%, #c9ad83 100%);
  }
  .contact {
    position: absolute;
    right: 16px; bottom: 22px;
    width: 230px;
    text-align: center;
    color: var(--ink);
    font-style: normal;
    font-size: 15px;
    font-weight: 600;
    line-height: 1.25;
  }
  .contact-web { font-size: 12px; }
  .contact-offer {
    display: inline-block;
    margin-top: 4px;
    color: var(--label-red);
    font-weight: 700;
    font-size: 14px;
  }

  /* Front cover */
  .cover-panel {
    left: 630px;
    background: var(--paper);
  }
  .cover-roof { position: absolute; left: 0; top: 0; }
  .cover-headline {
    position: absolute;
    left: 0; top: 58px; width: 300px;
    text-align: center;
    font-family: "Oswald", sans-serif;
    font-weight: 700;
    color: var(--paper);
    -webkit-text-stroke: 1px var(--outline);
    paint-order: stroke fill;
    text-shadow: 2px 2px 0 rgba(0,0,0,.45);
    line-height: 1.1;
  }
  .cover-tagline { font-size: 20px; display: block; }
  .cover-service { font-size: 30px; display: block; margin-top: 6px; letter-spacing: .5px; }
  .cover-photo {
    position: absolute;
    left: 0; top: 225px; width: 300px; height: 225px;
    background: linear-gradient(135deg, #4f7a36 0%, var(--shrub) 30%, #b88a55 50%, #7f9a55 70%, var(--lawn) 100%);
  }
  .cover-sweep { position: absolute; left: 0; top: 200px; }
  .brand {
    position: absolute;
    left: 50px; top: 510px;
    display: flex; align-items: center; gap: 10px;
  }
  .brand-square {
    width: 40px; height: 40px;
    background: var(--lime);
  }
  .brand-name {
    color: var(--brand-green);
    font-weight: 700;
    font-size: 30px;
    line-height: 1;
  }
  .brand-name small { display: block; font-size: 14px; letter-spacing: 1px; margin-top: 3px; }
</style>
</head>
<body>

  <section class="panel back-panel">
    <figure class="snapshot snapshot-beauty">
      <span class="snapshot-label">Add Beauty ...</span>
      <div class="snapshot-photo" role="img" aria-label="Curving grey concrete curb between mulch bed and lawn"></div>
    </figure>
    <figure class="snapshot snapshot-value">
      <span class="snapshot-label">Add Value ...</span>
      <div class="snapshot-photo" role="img" aria-label="Red stamped concrete curb edging a flower bed"></div>
    </figure>
    <div class="yard-photo" role="img" aria-label="Landscaped front yard with a sweeping curb around a mulch bed"></div>
    <address class="contact">
      418 Harlow Street West<br>
      Maple Ridge, WV 25990<br>
      800-617-4928<br>
      <span class="contact-web">www.brenwickyardworks.example</span><br>
      <span class="contact-offer">Free Estimates</span>
    </address>
  </section>

  <section class="panel cover-panel">
    <svg class="cover-roof" width="300" height="240" viewBox="0 0 300 240" aria-hidden="true">
      <polygon points="0,130 150,20 300,130 300,240 0,240" fill="var(--lawn)"/>
    </svg>
    <h1 class="cover-headline">
      <span class="cover-tagline">Give Your Yard<br>Some Curb Appeal!</span>
      <span class="cover-service">Concrete Curbing</span>
    </h1>
    <div class="cover-photo" role="img" aria-label="Shrubs and mulch beds edged by decorative concrete curbing"></div>
    <svg class="cover-sweep" width="300" height="300" viewBox="0 0 300 300" aria-hidden="true">
      <path d="M0,250 C90,200 200,290 300,200 L300,300 L0,300 Z" fill="var(--paper)"/>
    </svg>
    <div class="brand">
      <span class="brand-square"></span>
      <span class="brand-name">Brenwick<small>HOME SOLUTIONS</small></span>
    </div>
  </section>

</body>
</html>
```